Lorna Tess Tresses Fancy Business Card’s

I want my business cards to be elite, original and very classy. I want the business cards to match the colors of my logo and to match the design posted. I would love the design of the picture I posted

I want the card all white .
The dripping on the top of the card I want it to match the pink color in my logo that’s also posted .
I need my logo on the business card !
I need my Instagram- @lorna.tess.tresses__
And my phone number - 582 907 3365

Target Market(s)

My target market is young woman age 23 to older woman to the age of 65
I want both older and younger women to love my design . I don’t want any cheap looking business cards

Industry/Entity Type

Hair And Beauty

Contact Information for Business Card

Add my logo
Add my Instagram- @lorna.tess.tresses__
My number - 582 907 3365
My website- www.lornatesstresses.example

Font styles to use
Serif
Script

Colors
ffffff
e667a6
e34298

Requirements
Must have
• The business cards must have my logo, my number , my website, and my Instagram!
Nice to have
• Nice to have glitter words that match my logo
• The business cards must look classy and mature
• I want them to be very unique!!
Should not have
• Should not have any colors that doesn’t match my logo ! This is very important! Please

```html
<!DOCTYPE html>
<html lang="en">
<head>
<meta charset="utf-8">
<title>Lorna Tess Tresses – Business Card</title>
<link rel="stylesheet" href="https://fonts.googleapis.com/css2?family=Playfair+Display&family=Questrial&display=swap">
<style>
  :root {
    --pink: #e2449a;
    --pink-soft: #e667a6;
    --white: #ffffff;
    --silver: #cfcfcf;
    --ink: #4d4d4d;
    --backdrop: #ece7e2;
  }
  * { margin: 0; padding: 0; box-sizing: border-box; }
  html, body {
    width: 1189px;
    height: 1200px;
    overflow: hidden;
    background: var(--backdrop);
    font-family: "Questrial", "Century Gothic", sans-serif;
  }
  .canvas { position: relative; width: 1189px; height: 1200px; }
  .card {
    position: absolute;
    left: 169px;
    width: 851px;
    height: 485px;
    border-radius: 33px;
    box-shadow: 0 6px 18px rgba(0,0,0,0.18);
  }
  .card--front { top: 112px; background: var(--pink); }
  .card--back { top: 641px; background: var(--white); }

  .brand-name {
    position: absolute;
    left: 0; right: 0;
    top: 160px;
    text-align: center;
    font-family: "Playfair Display", "Times New Roman", serif;
    font-weight: 400;
    font-size: 68px;
    line-height: 78px;
    letter-spacing: 2px;
    color: var(--silver);
  }
  .brand-name span { display: block; }

  .contact-rule {
    position: absolute;
    left: 155px;
    top: 178px;
    width: 538px;
    height: 44px;
  }
  .contact-lines {
    position: absolute;
    left: 0; right: 0;
    top: 232px;
    text-align: center;
    color: var(--ink);
  }
  .handle { font-size: 25px; line-height: 34px; }
  .phone { font-size: 25px; line-height: 34px; letter-spacing: 1px; }
  .website {
    margin-top: 2px;
    font-size: 21px;
    line-height: 34px;
    letter-spacing: 8.6px;
  }
  .website .domain { color: var(--pink); }
</style>
</head>
<body>
<main class="canvas">
  <section class="card card--front">
    <p class="brand-name"><span>Lorna Tess</span><span>Tresses</span></p>
  </section>

  <section class="card card--back">
    <svg class="contact-rule" viewBox="0 0 538 44" aria-hidden="true">
      <line x1="0" y1="22" x2="194" y2="22" stroke="var(--pink)" stroke-width="3"/>
      <line x1="344" y1="22" x2="538" y2="22" stroke="var(--pink)" stroke-width="3"/>
      <circle cx="216" cy="22" r="20" fill="none" stroke="var(--pink)" stroke-width="2"/>
      <circle cx="216" cy="22" r="9" fill="var(--pink)"/>
      <circle cx="269" cy="22" r="20" fill="none" stroke="var(--pink)" stroke-width="2"/>
      <path d="M262 12 q-4 2 -2 10 q3 8 10 12 q3 1 5 -2 l-4 -4 q-2 1 -3 0 q-3 -3 -4 -7 q0 -1 1 -2 z" fill="none" stroke="var(--pink)" stroke-width="2" stroke-linejoin="round"/>
      <circle cx="322" cy="22" r="20" fill="none" stroke="var(--pink)" stroke-width="2"/>
      <circle cx="322" cy="22" r="11" fill="none" stroke="var(--pink)" stroke-width="1.6"/>
      <ellipse cx="322" cy="22" rx="5" ry="11" fill="none" stroke="var(--pink)" stroke-width="1.4"/>
      <line x1="311" y1="22" x2="333" y2="22" stroke="var(--pink)" stroke-width="1.4"/>
      <line x1="313" y1="16" x2="331" y2="16" stroke="var(--pink)" stroke-width="1.2"/>
      <line x1="313" y1="28" x2="331" y2="28" stroke="var(--pink)" stroke-width="1.2"/>
    </svg>
    <div class="contact-lines">
      <p class="handle">@lorna.tess.tresses__</p>
      <p class="phone">582 907 3365</p>
      <p class="website">www.<span class="domain">lornatesstresses</span>.example</p>
    </div>
  </section>
</main>
</body>
</html>
```